Bright Orbit IT company Soho london Stationary

We've just had a new logo designed on Pixel Harbor and we now need some Stationary to go with it.
We're a small IT support firm supporting Design companies in Soho London. Most of our clients work on Zorvas and a relatively creative so we want a relatively informal design on our stationary to reflect this.
We'd like to stick with the green in the logo but we're not adverse to adding another few colours to the palette.
Please see the attached file for our logo and not our website.

It Company

```html
<!DOCTYPE html>
<html lang="en">
<head>
<meta charset="utf-8">
<title>Bright Orbit Stationery</title>
<link rel="stylesheet" href="https://fonts.googleapis.com/css2?family=Open+Sans:wght@400;600;700&family=PT+Sans:wght@400&display=swap">
<style>
  :root {
    --green: #c0d93a;
    --black: #0d0d0d;
    --paper: #ffffff;
    --ink: #2b2b2b;
    --backdrop: #4a3a38;
    --signature-tone: #d9d9d9;
  }
  * { box-sizing: border-box; margin: 0; padding: 0; }
  html, body { width: 1200px; height: 890px; overflow: hidden; background: var(--backdrop); }
  .canvas { position: relative; width: 1200px; height: 890px; font-family: "Open Sans", Arial, sans-serif; color: var(--ink); }
  .sheet { position: absolute; background: var(--paper); box-shadow: 0 2px 6px rgba(0,0,0,.35); overflow: hidden; }

  .brand-name { font-family: "Open Sans", Arial, sans-serif; font-weight: 700; color: var(--green); white-space: nowrap; display: flex; align-items: center; gap: 6px; letter-spacing: -0.5px; }
  .brand-dot { display: inline-block; border-radius: 50%; background: var(--green); }
  .brand-name.on-green { color: var(--paper); }
  .brand-name.on-green .brand-dot { background: var(--paper); }

  .label { color: var(--green); }
  .contact { font-size: 6.5px; line-height: 8.5px; }

  .footer-band { position: absolute; left: 0; bottom: 0; width: 100%; display: block; }

  /* Business card front */
  .card-front { left: 91px; top: 83px; width: 247px; height: 142px; }
  .card-front .holder { position: absolute; right: 14px; top: 14px; text-align: right; }
  .card-front .holder-name { font-size: 9.5px; font-weight: 700; color: var(--black); }
  .card-front .holder-role { font-size: 7px; color: var(--green); }
  .card-front .brand-name { position: absolute; left: 11px; top: 63px; font-size: 18px; }
  .card-front .brand-dot { width: 9px; height: 9px; }
  .card-front .contact { position: absolute; left: 12px; top: 93px; }

  /* Business card back */
  .card-back { left: 353px; top: 86px; width: 247px; height: 141px; background: var(--green); }
  .card-back .brand-name { position: absolute; left: 0; width: 100%; top: 56px; justify-content: center; font-size: 22px; }
  .card-back .brand-dot { width: 11px; height: 11px; }
  .card-back .web { position: absolute; left: 0; width: 100%; top: 94px; text-align: center; color: var(--paper); font-size: 8px; letter-spacing: 2px; }

  /* Envelope back */
  .envelope-back { left: 89px; top: 298px; width: 602px; height: 263px; }
  .envelope-back .flap { position: absolute; left: 0; top: 0; width: 602px; height: 86px; display: block; }
  .envelope-back .flap-circle { position: absolute; left: 290px; top: 23px; width: 22px; height: 22px; border-radius: 50%; background: var(--paper); }
  .envelope-back .web { position: absolute; left: 0; width: 100%; top: 58px; text-align: center; color: var(--paper); font-size: 7.5px; letter-spacing: 2px; }

  /* Envelope front */
  .envelope-front { left: 36px; top: 403px; width: 603px; height: 262px; }
  .envelope-front .brand-name { position: absolute; left: 14px; top: 14px; font-size: 21px; }
  .envelope-front .brand-dot { width: 10px; height: 10px; }
  .envelope-front .contact { position: absolute; left: 14px; top: 51px; font-size: 7.5px; line-height: 11.5px; }

  /* Letterhead */
  .letterhead { left: 651px; top: 66px; width: 509px; height: 720px; }
  .letterhead .brand-name { position: absolute; left: 20px; top: 34px; font-size: 32px; }
  .letterhead .brand-dot { width: 14px; height: 14px; }
  .letter-body { position: absolute; left: 67px; top: 172px; width: 382px; font-family: "PT Sans", Arial, sans-serif; font-size: 7.9px; line-height: 8.3px; color: var(--ink); text-align: justify; hyphens: auto; }
  .letter-body p + p { margin-top: 8.3px; }
  .signature { position: absolute; left: 70px; top: 512px; width: 92px; height: 56px; background: var(--signature-tone); border-radius: 4px; }
  .letterhead .contact { position: absolute; left: 22px; top: 688px; font-size: 7.5px; line-height: 11.5px; }
  .letterhead .web { position: absolute; right: 28px; bottom: 4px; color: var(--paper); font-size: 8.5px; letter-spacing: 1.5px; }
</style>
</head>
<body>
<main class="canvas">

  <section class="sheet card-front" aria-label="Business card front">
    <div class="holder">
      <p class="holder-name">Owen Marsh</p>
      <p class="holder-role">Marketing Manager</p>
    </div>
    <div class="brand-name"><span>Bright Orbit</span><span class="brand-dot"></span></div>
    <div class="contact">
      <p class="label">Bright Orbit Ltd.</p>
      <p>42 Quill Lane, London, W1 4AB</p>
      <p><span class="label">Phone.</span> 0200 555 0147</p>
      <p><span class="label">Email.</span> info@bright-orbit.example</p>
    </div>
    <svg class="footer-band" viewBox="0 0 247 14" height="14" preserveAspectRatio="none" aria-hidden="true">
      <rect x="0" y="10" width="150" height="4" fill="var(--green)"/>
      <path d="M118 14 C130 14 134 5 146 5 L166 5 C156 5 150 14 140 14 Z" fill="var(--green)"/>
      <path d="M150 14 C160 14 164 3 176 3 L247 3 L247 14 Z" fill="var(--black)"/>
    </svg>
  </section>

  <section class="sheet card-back" aria-label="Business card back">
    <div class="brand-name on-green"><span>Bright Orbit</span><span class="brand-dot"></span></div>
    <p class="web">www.bright-orbit.example</p>
  </section>

  <section class="sheet envelope-back" aria-label="Envelope back">
    <svg class="flap" viewBox="0 0 602 86" preserveAspectRatio="none" aria-hidden="true">
      <path d="M0 0 L602 0 L602 50 Q600 66 585 70 L301 86 L17 70 Q2 66 0 50 Z" fill="var(--green)"/>
    </svg>
    <span class="flap-circle"></span>
    <p class="web">www.bright-orbit.example</p>
  </section>

  <section class="sheet envelope-front" aria-label="Envelope front">
    <div class="brand-name"><span>Bright Orbit</span><span class="brand-dot"></span></div>
    <div class="contact">
      <p class="label">Bright Orbit Ltd.</p>
      <p>42 Quill Lane, London, W1 4AB</p>
      <p><span class="label">Phone.</span> 0200 555 0147</p>
    </div>
    <svg class="footer-band" viewBox="0 0 603 22" height="22" preserveAspectRatio="none" aria-hidden="true">
      <rect x="0" y="16" width="400" height="6" fill="var(--green)"/>
      <path d="M355 22 C375 22 382 7 400 7 L430 7 C415 7 405 22 390 22 Z" fill="var(--green)"/>
      <path d="M400 22 C415 22 420 0 440 0 L603 0 L603 22 Z" fill="var(--black)"/>
    </svg>
  </section>

  <section class="sheet letterhead" aria-label="Letterhead">
    <div class="brand-name"><span>Bright Orbit</span><span class="brand-dot"></span></div>
    <div class="letter-body">
      <p>Lorem ipsum dolor sit amet, consectetuer adipiscing elit. Pellentesque tristique elementum sem. Quisque eget erat ac lectus sodales faucibus. Nam commodo est. Cras consequat faucibus velit. Nam ac magna. Sed et ligula. Nam volutpat, elit ac facilisis tempor, neque augue euismod leo, sit amet molestie sem est eu libero. Nulla facilisi. Pellentesque sit amet odio. Curabitur a leo consectetuer leo blandit porttitor. Pellentesque velit quam, gravida at, pharetra eu, convallis non, sem. Aenean tempor nibh at purus. Pellentesque porta. Suspendisse congue, lacus sit amet imperdiet imperdiet, urna massa rutrum urna, id elementum tellus diam quis risus.</p>
      <p>In dui turpis, varius vitae, tincidunt id, consequat ut, leo. Donec tincidunt tristique odio. Nulla erat felis, euismod nec, fringilla non, aliquet et, magna. Nulla at magna quis nisi pretium vehicula. Pellentesque habitant morbi tristique senectus et netus et malesuada fames ac turpis egestas. Class aptent taciti sociosqu ad litora torquent per conubia nostra, per inceptos himenaeos. In vel quam. Phasellus varius convallis purus. In non turpis. Nam sed risus. Etiam non neque at nisl gravida porttitor. Donec leo dolor, feugiat ut, pharetra et, porttitor a, metus. Suspendisse laoreet magna vel elit. Ut est augue, fermentum ac, molestie at, vestibulum et, urna.</p>
      <p>Nunc purus. Cras auctor. In ornare neque id ipsum. Nulla tincidunt, diam sit amet viverra euismod, sapien augue fringilla neque, at pellentesque felis tortor vel enim. Etiam dignissim. Sed a tortor vel nisl euismod ultricies. Donec molestie congue lectus. Integer sed turpis a tortor imperdiet consequat. Maecenas molestie placerat urna. Sed pede enim, sollicitudin nec, pretium nec, sollicitudin a, felis. In hac habitasse platea dictumst. Nam facilisis, tellus non scelerisque placerat, turpis turpis semper ante, euismod imperdiet augue nisi et neque. Vivamus tincidunt.</p>
      <p>Nulla lobortis ultricies nulla. Pellentesque purus mi, consequat quis, hendrerit sed, imperdiet non, eros. Nullam urna est, vehicula nec, cursus nec, dignissim sit amet, risus. Duis molestie, tellus sit amet laoreet ullamcorper, urna nisi fringilla ante, at rhoncus justo dolor vel dui. Nam hendrerit luctus lorem. Aenean tempor, metus vel posuere gravida, arcu nunc imperdiet tellus, ut blandit sem magna a turpis. Vivamus in neque. Lorem ipsum dolor sit amet, consectetuer adipiscing elit. Duis tristique tortor id nisl feugiat posuere. Maecenas posuere nisi ac risus. Nunc hendrerit. Praesent porta tempus ligula. Morbi in leo. Curabitur sapien nulla, cursus eget, faucibus in, porttitor et, odio. Praesent sed justo sed arcu commodo feugiat. Duis facilisis nulla ut eros. Cras libero. Donec mollis consectetuer metus. Praesent odio.</p>
    </div>
    <div class="signature" role="img" aria-label="Handwritten signature of the sender"></div>
    <div class="contact">
      <p class="label">Bright Orbit Ltd.</p>
      <p>42 Quill Lane, London, W1 4AB <span class="label">Phone.</span> 0200 555 0147</p>
    </div>
    <svg class="footer-band" viewBox="0 0 509 22" height="22" preserveAspectRatio="none" aria-hidden="true">
      <rect x="0" y="16" width="300" height="6" fill="var(--green)"/>
      <path d="M262 22 C280 22 286 7 302 7 L332 7 C318 7 310 22 296 22 Z" fill="var(--green)"/>
      <path d="M305 22 C320 22 325 1 345 1 L509 1 L509 22 Z" fill="var(--black)"/>
    </svg>
    <p class="web">www.bright-orbit.example</p>
  </section>

</main>
</body>
</html>
```